Gutschein-Design für Badmodernisierungen
Zielgruppe
wir modernisieren Heizungen und Bäder; Zielgruppe sind Häuserbesitzer sowie Hausverwaltungen die Ihre Heizung modernisieren lassen wollen.
Aufgabenstellung
Wir haben in diesem Jahr unser 15. Jubiläum und wollen unseren Angeboten ein Flyer/Gutschein Beilegen der das Kaufen interessanter macht.
Wir bieten bei Installation einer neuen Heizung & Abschluss eines Wartungsvertrages diesen Wartungsvertrag für 1 bzw 2 Jahre Kostenlos. Wichtig ist Postkartenformat wo auf der Rückseite wie eine Postkarte aufgebaut ist mit Adressfeld und auf der anderen Seite nochmal Text( Gutschein.....) und Platz für das Kleingedruckte
Wichtig Hauptlogo ist das RMP GmbH Logo
Das Rohrfuchs.profi Logo ist unsere App und Plaudernetzauftritt bitte kurz auf die App hinweisen mit einem kleinem Button

```html
<!DOCTYPE html>
<html lang="de">
<head>
<meta charset="utf-8">
<title>RMP GmbH – Gutschein Postkarte</title>
<link href="https://fonts.googleapis.com/css2?family=Kaushan+Script&family=Montserrat:wght@300;400;700&display=swap" rel="stylesheet">
<style>
  :root {
    --orange: #e85c0d;
    --ink: #3a3a3a;
    --grey: #7a7a7a;
    --line: #9a9a9a;
    --black: #050505;
    --slate: #1b232b;
    --white: #ffffff;
    --page: #ffffff;
  }
  * { margin: 0; padding: 0; box-sizing: border-box; }
  html, body { width: 849px; height: 1200px; overflow: hidden; background: var(--page); }
  body { position: relative; font-family: "Montserrat", sans-serif; color: var(--ink); }

  .card { position: absolute; left: 34px; width: 780px; height: 554px; overflow: hidden; }
  .card--front { top: 30px; background: var(--black); }
  .card--back { top: 616px; background: var(--white); border: 1px solid #d8d8d8; }

  /* front */
  .front-photo {
    position: absolute; inset: 0;
    background: linear-gradient(135deg, var(--slate) 0%, var(--black) 70%);
  }
  .brand-box {
    position: absolute; left: 562px; top: 26px; width: 202px; height: 86px;
    background: #161616; display: flex; align-items: center; justify-content: center;
  }
  .brand-box__name { font-weight: 700; font-size: 30px; color: var(--white); letter-spacing: 1px; }

  .voucher-circle {
    position: absolute; left: 336px; top: 175px; width: 396px; height: 396px;
    border-radius: 50%; background: var(--orange);
  }
  .voucher-title { position: absolute; font-family: "Kaushan Script", cursive; color: var(--white); line-height: 1; }
  .voucher-title--ihr { left: 425px; top: 200px; font-size: 80px; }
  .voucher-title--gutschein { left: 330px; top: 280px; font-size: 92px; }
  .voucher-sub { position: absolute; left: 421px; top: 378px; font-weight: 300; font-size: 25px; color: var(--white); }

  /* back */
  .seal {
    position: absolute; left: 26px; top: 34px; width: 121px; height: 121px; border-radius: 50%;
    background: var(--orange); color: var(--white); text-align: center;
  }
  .seal__script { position: absolute; left: 0; right: 0; font-family: "Kaushan Script", cursive; line-height: 1; }
  .seal__ihr { top: 22px; font-size: 26px; }
  .seal__gutschein { top: 50px; font-size: 21px; }
  .seal__name { position: absolute; left: 0; right: 0; top: 82px; font-size: 9px; font-weight: 400; }

  .back-headline { position: absolute; left: 159px; top: 60px; font-weight: 700; font-size: 17px; line-height: 1.22; color: var(--orange); }
  .back-text { position: absolute; left: 30px; width: 360px; }
  .offer-title { top: 176px; font-weight: 700; font-size: 15px; line-height: 1.3; color: var(--ink); }
  .offer-body { top: 230px; font-weight: 300; font-size: 13.2px; line-height: 1.32; color: var(--grey); }
  .offer-quote { top: 300px; font-weight: 300; font-size: 13.2px; line-height: 1.32; color: var(--orange); }
  .offer-sign { top: 390px; font-weight: 300; font-size: 13.2px; line-height: 1.32; color: var(--grey); }
  .small-print { top: 440px; font-weight: 300; font-size: 8px; line-height: 1.4; color: var(--grey); }

  .divider { position: absolute; left: 397px; top: 60px; width: 1px; height: 458px; background: var(--line); }
  .sender {
    position: absolute; left: 404px; top: 486px; transform-origin: 0 0; transform: rotate(-90deg);
    font-weight: 300; font-size: 8.5px; color: var(--grey); white-space: nowrap;
  }
  .address-line { position: absolute; left: 429px; width: 303px; height: 1px; background: var(--line); }

  .app-button {
    position: absolute; left: 429px; top: 442px; width: 50px; height: 50px;
    border: 1px solid #c8c8c8; border-radius: 10px; background: var(--white);
  }
  .app-info { position: absolute; left: 490px; top: 442px; width: 260px; font-weight: 300; font-size: 8.2px; line-height: 1.35; color: var(--grey); }
  .app-info strong { display: block; font-weight: 700; font-size: 9.5px; color: var(--ink); }
</style>
</head>
<body>

<section class="card card--front" aria-label="Vorderseite">
  <div class="front-photo" role="img" aria-label="Foto: brennendes Streichholz mit bläulichem Rauch auf schwarzem Grund"></div>
  <div class="brand-box"><span class="brand-box__name">RMP GmbH</span></div>
  <div class="voucher-circle"></div>
  <div class="voucher-title voucher-title--ihr">Ihr</div>
  <div class="voucher-title voucher-title--gutschein">Gutschein</div>
  <div class="voucher-sub">bei einer neue Heizung</div>
</section>

<section class="card card--back" aria-label="Rückseite">
  <div class="seal">
    <span class="seal__script seal__ihr">Ihr</span>
    <span class="seal__script seal__gutschein">Gutschein</span>
    <span class="seal__name">RMP GmbH</span>
  </div>
  <p class="back-headline">Seit 15 Jahren<br>Ihr zuverlässiger Partner<br>für Heizung und Bad.</p>

  <p class="back-text offer-title">Gutschein für einen kostenlosen<br>Wartungsvertrag für Ihre neue Heizung</p>
  <p class="back-text offer-body">Während unseres Jubiläum Jahres bieten wir<br>Ihnen bei Installation einer neuen Heizung &amp;<br>Abschluss einen Wartungsvertrag Kostenlos.</p>
  <p class="back-text offer-quote">«Wir achten auf Nachhaltigkeit und sinnvollen<br>Einsatz wertvoller Rohstoffe. Moderne Haus-<br>technik arbeitet zuverlässig, schont die Umwelt<br>und Ihren Geldbeutel.»</p>
  <p class="back-text offer-sign">Wir freuen uns auf die Partnerschaft mit Ihnen<br>Jonas Feldkamp - Geschäftsführer</p>
  <p class="back-text small-print">Das Kleingedruckte: Der Gutschein gilt nur bei Installation einer neuen Heizung und gleichzeitigem Abschluss eines Wartungsvertrags. Keine Barauszahlung möglich. Nicht mit anderen Aktionen kombinierbar. Gültig bis zum Ende des Jubiläumsjahres.</p>

  <div class="divider"></div>
  <p class="sender">RMP GmbH · Brunnenweg 12 · 70599 Musterstadt · www.rmp-musterstadt.de</p>

  <div class="address-line" style="top:226px"></div>
  <div class="address-line" style="top:284px"></div>
  <div class="address-line" style="top:342px"></div>
  <div class="address-line" style="top:400px"></div>

  <div class="app-button"></div>
  <p class="app-info"><strong>Smartphone App</strong>Rohrfuchs.profi gibt es auch als Smartphone-App!<br>Sie ist die Drehscheibe für aktuelle Informationen und<br>der direkte Draht zu uns. Kostenlos!</p>
</section>

</body>
</html>
```